Company or website name
- Resume for accounting
- Links to the website
- http://www.gestiondelvallenorte.com/#bienvenidos
- Describe your company and organization and target audience
- The web layout is not for a business. This is a personal site that will present my CV. I am an accountant. It would be nice to follow a model like this website: http://www.gestiondelvallenorte.com/#bienvenidos . The main users of the site will be recruiters.
- The design should have the following
- The design must be modern . There must be both personal photos and scenes work as an office and buildings.

```html
<!DOCTYPE html>
<html lang="en">
<head>
<meta charset="utf-8">
<title>Resume for Accounting – Education</title>
<link rel="stylesheet" href="https://fonts.googleapis.com/css2?family=Alegreya:ital,wght@1,400;1,700&display=swap">
<style>
  :root {
    --bg: #000000;
    --text: #ffffff;
    --rail-light: #7a7a7a;
    --rail-dark: #1a1a1a;
    --art-light: #4a4a4a;
    --art-mid: #2a2a2a;
    --art-edge: #141414;
  }
  * { margin: 0; padding: 0; box-sizing: border-box; }
  html, body {
    width: 1200px;
    height: 675px;
    overflow: hidden;
    background: var(--bg);
  }
  .page {
    position: relative;
    width: 1200px;
    height: 675px;
    background: var(--bg);
    color: var(--text);
    font-family: "Alegreya", Georgia, serif;
  }
  .side-rail {
    position: absolute;
    left: 43px;
    top: 0;
    width: 5px;
    height: 675px;
    background: linear-gradient(to bottom, var(--rail-dark) 0%, var(--rail-light) 45%, var(--rail-light) 55%, var(--rail-dark) 100%);
    opacity: 0.8;
  }
  .main-nav {
    position: absolute;
    left: 45px;
    top: 135px;
    width: 160px;
    list-style: none;
    text-align: center;
  }
  .main-nav li {
    height: 26.4px;
    font-style: italic;
    font-size: 14.5px;
    letter-spacing: 1.2px;
    text-transform: uppercase;
  }
  .main-nav a {
    color: var(--text);
    text-decoration: none;
  }
  .main-nav .is-current a { text-decoration: underline; text-underline-offset: 3px; }
  .main-nav .is-bold a { font-weight: 700; }
  .education {
    position: absolute;
    left: 387px;
    top: 143px;
    font-style: italic;
    font-weight: 700;
    font-size: 16.5px;
    letter-spacing: 1.6px;
    line-height: 18.8px;
    text-transform: uppercase;
    font-variant-numeric: oldstyle-nums;
  }
  .education p + p { margin-top: 18.8px; }
  .subject-art {
    position: absolute;
    left: 462px;
    top: 287px;
    width: 520px;
    height: 320px;
    border-radius: 14px;
    background: radial-gradient(ellipse at 50% 50%, var(--art-light) 0%, var(--art-mid) 45%, var(--art-edge) 80%, var(--bg) 100%);
  }
</style>
</head>
<body>
  <div class="page">
    <div class="side-rail"></div>

    <ul class="main-nav">
      <li class="is-bold"><a href="#summary">Summary</a></li>
      <li><a href="#highlights">Highlits</a></li>
      <li><a href="#experience">Experience</a></li>
      <li class="is-current"><a href="#education">Education</a></li>
      <li><a href="#contact">Contact</a></li>
    </ul>

    <section class="education" id="education">
      <p>2003 Harlow State University St. Louis, MO<br>Bachelor of Science Accounting</p>
      <p>Coursework in Asset Protection and Tax Strategies<br>Recipient of Eleanor Whitcombe Scholarship</p>
    </section>

    <div class="subject-art" role="img" aria-label="Hand-drawn chalk diagram: the word Accounting in an oval with arrows to financial, verification, expense, report, balance sheet, income, revenue, management, information, assets, credit and records"></div>
  </div>
</body>
</html>
```